New Business Card Design for Engineering and Surveying Company

We need a new design template for our business cards. We are a civil engineering, land surveying and pipeline integrity business. Please see brqholt.com for details. We need a bold, new business card design to complement our rebranding and marketing program. We have anew logo and attached vectro file. Please find additional details below. I am available to answer any questions.

Target Market(s)

Contractors, business owners, oil companies

Contact Information for Business Card

Needs to be customizable for different people (name, title, cell)

Font styles to use
Sans Serif
Other font styles liked:
• See eps file

Requirements
Must have
• Example Information:
Derek Fannaby

T:409-555-0187
M: 202-555-0143
dfannaby@brqholt.com

Address: 1870 Corvane Parkway, Beaumont, Texas 77701
Email: dfanbagy@brqholt.com
Website: www.brqholt.com
Nice to have
• I would like the back of the card to have the logo on a bold background with the text below:

[logo]
ROLAND FANNABY & ASSOCIATES
CIVIL ENGINEERING | LAND SURVEYING | PIPELINE INTEGRITY

The reverse side should have the contact information for the person (example above), a smaller version of the logo and a graphic

```html
<!DOCTYPE html>
<html lang="en">
<head>
<meta charset="utf-8">
<title>RFA Business Card</title>
<link rel="stylesheet" href="https://fonts.googleapis.com/css2?family=Montserrat:wght@600;700;800&family=Varela+Round&display=swap">
<style>
  :root {
    --backdrop: #3a3a3a;
    --brand-blue: #234d9e;
    --brand-red: #e4202f;
    --card-white: #ffffff;
    --card-black: #000000;
    --ink-dark: #111111;
  }
  * { margin: 0; padding: 0; box-sizing: border-box; }
  html, body { width: 1200px; height: 1200px; overflow: hidden; }
  body { background: var(--backdrop); position: relative; }

  .card { position: absolute; overflow: hidden; }
  .card-front { left: 290px; top: 177px; width: 626px; height: 358px; background: var(--card-white); }
  .card-back { left: 292px; top: 642px; width: 624px; height: 357px; background: var(--card-black); }

  .corner-shapes { position: absolute; inset: 0; width: 100%; height: 100%; }

  .brand-mark { position: absolute; display: flex; align-items: center; }
  .brand-square { display: block; }
  .brand-name { font-family: "Montserrat", sans-serif; font-weight: 800; line-height: 1; letter-spacing: 1px; }

  .card-front .brand-mark { left: 66px; top: 58px; gap: 14px; }
  .card-front .brand-square { width: 18px; height: 18px; background: var(--brand-red); }
  .card-front .brand-name { font-size: 58px; color: var(--brand-blue); }
  .front-company { position: absolute; left: 90px; top: 116px; font-family: "Montserrat", sans-serif; font-weight: 700; font-size: 10.5px; color: var(--ink-dark); letter-spacing: 0.2px; }

  .contact-list { position: absolute; left: 51px; top: 157px; list-style: none; }
  .contact-list li { display: flex; align-items: center; height: 29.5px; font-family: "Varela Round", sans-serif; font-size: 18.5px; color: var(--brand-blue); letter-spacing: 0.3px; }
  .contact-icon { width: 18px; height: 18px; margin-right: 12px; flex: none; fill: var(--brand-blue); }

  .person { position: absolute; left: 446px; top: 156px; }
  .person-name { font-family: "Montserrat", sans-serif; font-weight: 700; font-size: 17.5px; color: var(--brand-red); padding-bottom: 2px; border-bottom: 2.5px solid var(--brand-blue); white-space: nowrap; }
  .person-title { font-family: "Varela Round", sans-serif; font-size: 17px; color: var(--brand-blue); margin-top: 4px; }

  .address { position: absolute; right: 195px; top: 299px; text-align: right; font-family: "Varela Round", sans-serif; font-size: 17.5px; line-height: 21px; color: var(--brand-blue); letter-spacing: 0.3px; }
  .address-pin { width: 15px; height: 19px; fill: var(--brand-blue); vertical-align: -2px; margin-right: 3px; }

  .card-back .brand-mark { left: 150px; top: 104px; gap: 26px; }
  .card-back .brand-square { width: 42px; height: 42px; background: var(--brand-red); }
  .card-back .brand-name { font-size: 100px; color: var(--card-white); }
  .back-company { position: absolute; left: 0; right: 40px; top: 226px; text-align: center; padding-left: 90px; font-family: "Montserrat", sans-serif; font-weight: 700; font-size: 18px; color: var(--card-white); letter-spacing: 0.2px; }
  .service-band { position: absolute; left: 40px; top: 286px; width: 542px; height: 46px; background: var(--brand-blue); display: flex; align-items: center; justify-content: center; font-family: "Montserrat", sans-serif; font-weight: 700; font-size: 15.5px; color: var(--card-white); white-space: nowrap; }
</style>
</head>
<body>

<section class="card card-front">
  <svg class="corner-shapes" viewBox="0 0 626 358" preserveAspectRatio="none" aria-hidden="true">
    <polygon points="0,0 51,0 0,142" fill="var(--brand-red)"/>
    <polygon points="486,0 626,0 626,51" fill="var(--brand-blue)"/>
    <polygon points="0,306 140,358 0,358" fill="var(--brand-blue)"/>
    <polygon points="626,219 626,358 575,358" fill="var(--brand-red)"/>
  </svg>

  <div class="brand-mark">
    <span class="brand-square"></span>
    <span class="brand-name">RFA</span>
  </div>
  <p class="front-company">ROLAND FANNABY &amp; ASSOCIATES</p>

  <ul class="contact-list">
    <li>
      <svg class="contact-icon" viewBox="0 0 24 24" aria-hidden="true"><path d="M6.6 10.8a15.2 15.2 0 0 0 6.6 6.6l2.2-2.2c.3-.3.7-.4 1-.2 1.1.4 2.3.6 3.6.6.6 0 1 .4 1 1V20c0 .6-.4 1-1 1A17 17 0 0 1 3 4c0-.6.4-1 1-1h3.5c.6 0 1 .4 1 1 0 1.3.2 2.5.6 3.6.1.3 0 .7-.2 1z"/></svg>
      409-555-0187
    </li>
    <li>
      <svg class="contact-icon" viewBox="0 0 24 24" aria-hidden="true"><path d="M8 1h8a2 2 0 0 1 2 2v18a2 2 0 0 1-2 2H8a2 2 0 0 1-2-2V3a2 2 0 0 1 2-2zm0 3v15h8V4zm4 16.2a.9.9 0 1 0 0 1.8.9.9 0 0 0 0-1.8z"/></svg>
      202-555-0143
    </li>
    <li>
      <svg class="contact-icon" viewBox="0 0 24 24" aria-hidden="true"><path d="M2 9l10-6 10 6v11a1 1 0 0 1-1 1H3a1 1 0 0 1-1-1zm2 1.3V19h16v-8.7l-8 5zM6 9v1.2l6 3.7 6-3.7V9zm1.5 0h9v1h-9z"/></svg>
      dfanbagy@brqholt.com
    </li>
    <li>
      <svg class="contact-icon" viewBox="0 0 24 24" aria-hidden="true"><path d="M12 2a10 10 0 1 0 0 20 10 10 0 0 0 0-20zm0 2a8 8 0 0 1 7.4 5h-3.2l-1.7 2 1.5 3-2 3v2.8A8 8 0 0 1 4.3 9.8L7 10l2 2-1 3 2 2v2.8A8 8 0 0 1 12 4zm-3 2-1 2 2 1 2-2-1-1z"/></svg>
      www.brqholt.com
    </li>
  </ul>

  <div class="person">
    <p class="person-name">Derek Fannaby</p>
    <p class="person-title">CEO</p>
  </div>

  <p class="address">
    <svg class="address-pin" viewBox="0 0 16 20" aria-hidden="true"><path d="M8 0a7 7 0 0 0-7 7c0 5 7 13 7 13s7-8 7-13a7 7 0 0 0-7-7zm0 4a3 3 0 1 1 0 6 3 3 0 0 1 0-6z"/></svg>1870 Corvane Parkway,<br>Beaumont, Texas 77701
  </p>
</section>

<section class="card card-back">
  <div class="brand-mark">
    <span class="brand-square"></span>
    <span class="brand-name">RFA</span>
  </div>
  <p class="back-company">ROLAND FANNABY &amp; ASSOCIATES</p>
  <div class="service-band">CIVIL ENGINEERING | LAND SURVEYING | PIPELINE INTEGRITY</div>
</section>

</body>
</html>
```